HK-Steuerberatung WordPress Site fully implemented (tax advisor)

Hello!
I need a little Wordpress Site for my newly founded Tax-Advisor Company.
I am a one-man Office advising in the area of Crypto-Currency.
PLEASE only provide a Design, if you can also Implement a WP-Site afterwards on an existing Webspace.

Please find the Content and Website-Description in the attached Document

Language for the Website is German (for now)

Target Market(s)

Tax-Advisory (specialized in Crypto Currency)

Coding

Coded - Design and coding required

Number of Pages Required

5+ page

Font styles to use
Sans Serif

Requirements
Must have
• Wordpress Implementation afterwards - Details according to attached Project Information Document

```html
<!DOCTYPE html>
<html lang="de">
<head>
<meta charset="utf-8">
<title>HK-Steuerberatung</title>
<link href="https://fonts.googleapis.com/css2?family=Montserrat:wght@300;400;700&family=Fira+Sans+Condensed:wght@400;500&family=Catamaran:wght@400&display=swap" rel="stylesheet">
<style>
:root{
  --night:#02050c;
  --navy:#1b2941;
  --navy-card:#1c2a45;
  --paper:#f2f0f1;
  --white:#ffffff;
  --ink:#1c2a44;
  --black:#000000;
  --rule:#3a4761;
}
*{margin:0;padding:0;box-sizing:border-box}
html,body{width:955px;height:1200px;overflow:hidden}
body{position:relative;background:var(--paper);font-family:"Fira Sans Condensed",sans-serif;color:var(--white)}
.hero{position:absolute;left:0;top:0;width:955px;height:522px;background:var(--night);overflow:hidden}
.hero-visual{position:absolute;left:0;top:320px;width:955px;height:202px;
  background:radial-gradient(ellipse 420px 90px at 330px 110px,rgba(70,100,150,.55),rgba(20,35,70,.35) 60%,transparent 100%),
             linear-gradient(180deg,rgba(2,5,12,0) 0%,#10203f 100%)}
.brand{position:absolute;display:flex;align-items:center;gap:8px;font-family:"Montserrat",sans-serif;font-weight:700;color:var(--white);letter-spacing:.3px}
.brand-mark{width:18px;height:18px;background:var(--white)}
.brand.top{left:115px;top:32px;font-size:14px}
.nav{position:absolute;top:35px;left:0;width:955px;height:20px;font-size:13.5px}
.nav a{position:absolute;top:0;color:var(--white);text-decoration:none;white-space:nowrap}
.nav a.active{border-bottom:2px solid var(--white);padding-bottom:1px}
.lang{position:absolute;left:820px;top:36px;width:16px;height:16px;border-radius:50%;background:linear-gradient(180deg,#b22234 0 50%,#fff 50% 60%,#b22234 60% 75%,#fff 75%);overflow:hidden}
.lang::before{content:"";position:absolute;left:0;top:0;width:8px;height:8px;background:#3c3b6e}
.hero-text{position:absolute;left:0;top:155px;width:955px;text-align:center}
.hero-kicker{font-family:"Montserrat",sans-serif;font-weight:300;font-size:29px;line-height:36px}
.hero-title{font-family:"Montserrat",sans-serif;font-weight:700;font-size:42px;line-height:52px;letter-spacing:-.5px}
.hero-lead{margin-top:12px;font-size:13.5px;line-height:22px}
.hero-btn{display:inline-block;margin-top:15px;background:var(--white);color:var(--ink);font-family:"Montserrat",sans-serif;font-size:13px;padding:7px 14px;border-radius:4px}
.quotes{position:absolute;left:0;top:522px;width:955px;height:420px}
.quotes h2{position:absolute;top:32px;width:955px;text-align:center;font-family:"Montserrat",sans-serif;font-weight:700;font-size:29px;color:var(--ink)}
.card{position:absolute;top:105px;width:230px;height:226px;border-radius:11px;background:var(--white);color:var(--ink);display:flex;align-items:center;justify-content:center;text-align:center;padding:0 19px;font-family:"Catamaran",sans-serif;font-size:22px;line-height:32px;overflow-wrap:anywhere;box-shadow:0 1px 4px rgba(0,0,0,.05)}
.card.dark{background:var(--navy-card);color:var(--white)}
.footer{position:absolute;left:0;top:942px;width:955px;height:258px;background:var(--navy)}
.brand.bottom{left:375px;top:38px;font-size:14px}
.foot-nav{position:absolute;top:92px;left:291px;display:flex;font-size:14px}
.foot-nav a{color:var(--white);text-decoration:none;margin-right:30px}
.subscribe{position:absolute;left:115px;top:146px;display:flex;align-items:center}
.subscribe-label{font-size:13px;font-weight:500;letter-spacing:-.2px;width:193px}
.email-field{width:208px;height:31px;background:var(--white);color:#b9b9b9;font-size:13px;padding:7px 8px}
.subscribe-btn{margin-left:14px;height:31px;width:105px;background:var(--black);border-left:5px solid var(--white);border-right:5px solid var(--white);display:flex;align-items:center;justify-content:center;font-size:12.5px;font-weight:500}
.contact{position:absolute;left:681px;top:138px;font-size:14px;line-height:27px}
.contact div{display:flex;align-items:center;gap:9px}
.foot-rule{position:absolute;left:0;top:213px;width:955px;height:1px;background:var(--rule)}
.copyright{position:absolute;top:226px;width:955px;text-align:center;font-size:10.5px;padding-left:15px}
</style>
</head>
<body>
<header class="hero">
  <div class="hero-visual" role="img" aria-label="Leuchtende Partikelringe als Hintergrundbild"></div>
  <div class="brand top"><span class="brand-mark"></span>HK STEUERBERATUNG</div>
  <nav class="nav">
    <a class="active" style="left:433px">Home</a>
    <a style="left:495px">Leistungen ⌄</a>
    <a style="left:585px">Über mich</a>
    <a style="left:671px">Kontakt</a>
    <a style="left:737px">Impressum</a>
  </nav>
  <span class="lang" aria-label="English"></span>
  <div class="hero-text">
    <p class="hero-kicker">Willkommen bei</p>
    <h1 class="hero-title">HK-Steuerberatung!</h1>
    <p class="hero-lead">Ihrem Spezialisten bei allen steuerlichen Themen rund<br>um Einkünfte &amp; Vermögen aus Krypto-Assets.</p>
    <span class="hero-btn">Weiter zu unseren Leistungen</span>
  </div>
</header>

<section class="quotes">
  <h2>Zitat</h2>
  <div class="card dark" style="left:115px">Dann mach ich eine Schweizer Holding-Gesellschaft– dort zahlt man fast keine Steuern</div>
  <div class="card" style="left:361px">Dann melde ich einfach meinen Hauptwohnsitz in Österreich ab</div>
  <div class="card" style="left:607px">Dann lass ich meine Kryptos auf einer Börse in Svingapur, dort ist das steuerfrei</div>
</section>

<footer class="footer">
  <div class="brand bottom"><span class="brand-mark"></span>HK STEUERBERATUNG</div>
  <nav class="foot-nav"><a>Home</a><a>Leistungen</a><a>Über mich</a><a>Kontakt</a><a>Impressum</a></nav>
  <div class="subscribe">
    <span class="subscribe-label">ABONNIEREN SIE UNSEREN BLOG</span>
    <span class="email-field">Email</span>
    <span class="subscribe-btn">Subscribe</span>
  </div>
  <div class="contact">
    <div><svg width="13" height="13" viewBox="0 0 24 24" fill="none" stroke="#fff" stroke-width="1.8"><path d="M5 3h4l2 5-3 2a12 12 0 0 0 6 6l2-3 5 2v4a2 2 0 0 1-2 2A17 17 0 0 1 3 5a2 2 0 0 1 2-2z"/></svg>+43 512 604 187</div>
    <div><svg width="13" height="10" viewBox="0 0 24 18" fill="#fff"><path d="M0 0h24v2L12 10 0 2z"/><path d="M0 5l12 8 12-8v13H0z"/></svg>office@hk-steuer.example</div>
  </div>
  <div class="foot-rule"></div>
  <p class="copyright">© copyrights 2022 HK Steuerberatung | &nbsp;All Rights Reserved</p>
</footer>
</body>
</html>
```